Business card design for a Cloud Service Provider Company

We already have business card and would like to update and get a different design. Our company is Managed IT services and Cloud Solutions Company, Tevro Systems. Attached is our current logo, current business card and sample design. I am not sure if we still need to keep our partners details on the back of the card as it does not look good to me... Please let me know if you need any additional information...

Target Market(s)

Any verticals with IT infrastructure - CEOs, CFOs and CIOs

Industry/Entity Type

Information Technology

Requirements
Must have
• First Name Last Name
• Phone
• Email address
• Company Logo

```html
<!DOCTYPE html>
<html lang="en">
<head>
<meta charset="utf-8">
<title>Tevro Systems – Business Card</title>
<link href="https://fonts.googleapis.com/css2?family=Montserrat:wght@500;600;700&display=swap" rel="stylesheet">
<style>
  :root {
    --page-bg: #ffffff;
    --ink: #2a2a2a;
    --card-edge: #d4d4d4;
    --white: #ffffff;
    --grad-blue: #45a6e2;
    --grad-sky: #52b8f2;
    --grad-cyan: #5ad6e3;
    --grad-green: #66f78e;
  }
  html, body {
    margin: 0;
    padding: 0;
    overflow: hidden;
    background: var(--page-bg);
  }
  .canvas {
    position: relative;
    width: 1200px;
    height: 1198px;
    overflow: hidden;
    background: var(--page-bg);
    font-family: "Montserrat", sans-serif;
  }
  .card {
    position: absolute;
    left: 163px;
    width: 878px;
    height: 488px;
    box-sizing: border-box;
  }
  /* Front face */
  .card-front {
    top: 85px;
    border: 1.5px solid var(--card-edge);
    border-top-right-radius: 95px;
    background: var(--white);
  }
  .front-brand {
    position: absolute;
    left: 0;
    right: 0;
    top: 160px;
    text-align: center;
    font-weight: 600;
    font-size: 96px;
    line-height: 1;
    letter-spacing: -0.01em;
    color: var(--ink);
  }
  .front-details {
    position: absolute;
    left: 0;
    right: 0;
    top: 400px;
    text-align: center;
    font-weight: 700;
    font-size: 17px;
    line-height: 31px;
    letter-spacing: 0.03em;
    text-transform: uppercase;
    color: var(--ink);
  }
  .front-details .gap { display: inline-block; width: 14px; }
  /* Back face */
  .card-back {
    top: 599px;
    border-top-left-radius: 95px;
    background: linear-gradient(125deg, var(--grad-blue) 0%, var(--grad-sky) 32%, var(--grad-cyan) 65%, var(--grad-green) 100%);
    color: var(--white);
  }
  .back-brand {
    position: absolute;
    left: 38px;
    top: 52px;
    font-weight: 600;
    font-size: 38px;
    line-height: 1;
    color: var(--white);
  }
  .identity {
    position: absolute;
    right: 70px;
    top: 196px;
    text-align: right;
    text-transform: uppercase;
  }
  .identity .person-name {
    margin: 0;
    font-weight: 600;
    font-size: 38px;
    line-height: 44px;
    letter-spacing: 0.07em;
  }
  .identity .job-title {
    margin: 2px 0 0;
    font-weight: 500;
    font-size: 26px;
    line-height: 32px;
    letter-spacing: 0.07em;
  }
  .contact {
    position: absolute;
    right: 70px;
    top: 366px;
    margin: 0;
    padding: 0;
    list-style: none;
    text-align: right;
    font-weight: 600;
    font-size: 16.5px;
    line-height: 28.5px;
    letter-spacing: 0.04em;
    text-transform: uppercase;
  }
</style>
</head>
<body>
<main class="canvas">
  <section class="card card-front" aria-label="Card front">
    <div class="front-brand">Tevro</div>
    <div class="front-details">
      <div>Level 14, 88 Harbour Lane Sydney, NSW 2000</div>
      <div>www.tevrosys.com.au<span class="gap"></span>Support: 1300 555 210</div>
    </div>
  </section>

  <section class="card card-back" aria-label="Card back">
    <div class="back-brand">Tevro</div>
    <div class="identity">
      <p class="person-name">Milo R. Dassen</p>
      <p class="job-title">Technical Manager</p>
    </div>
    <ul class="contact">
      <li>milo.dassen@tevrosys.com.au</li>
      <li>P: +51 2 5550 1042</li>
      <li>M: +51 400 555 318</li>
    </ul>
  </section>
</main>
</body>
</html>
```